Bref créative
K Dorsey Septic Solutions LLC.
Facebook
I would like a nice clean looking backround for my timeline on my facebook. I want to use my logo in it somehow. You can look at my facebook now to see my logo and get an idea of the type of work we do.
www.facebook.com/kdseptic
Utilities
Homeowners
Use logo
I can send a 2 color logo file to anyone.
logo file
2 color logo file
AI format logo
2 color
AI Format logo

```html
<!DOCTYPE html>
<html lang="en">
<head>
<meta charset="UTF-8">
<title>K Dorsey Septic Solutions LLC. – Timeline Cover</title>
<link href="https://fonts.googleapis.com/css2?family=Archivo+Black&display=swap" rel="stylesheet">
<style>
  :root {
    --concrete-light: #d6d3cd;
    --concrete-mid: #c4c1bb;
    --concrete-dark: #a9a6a0;
    --ink: #0b0b0b;
    --brand-blue: #1d4f8f;
    --brand-green: #4f8a2c;
  }
  html, body {
    margin: 0;
    padding: 0;
    width: 1200px;
    height: 444px;
    overflow: hidden;
  }
  .cover {
    position: relative;
    width: 1200px;
    height: 444px;
    overflow: hidden;
    font-family: "Archivo Black", "Arial Black", sans-serif;
  }
  .cover__texture {
    position: absolute;
    inset: 0;
    background:
      radial-gradient(ellipse at 30% 40%, var(--concrete-light) 0%, transparent 60%),
      radial-gradient(ellipse at 80% 70%, var(--concrete-mid) 0%, transparent 65%),
      linear-gradient(160deg, var(--concrete-light) 0%, var(--concrete-mid) 55%, var(--concrete-dark) 100%);
  }
  .brand {
    position: absolute;
    left: 19px;
    top: 112px;
    width: 330px;
    text-align: center;
    color: var(--brand-blue);
  }
  .brand__dot {
    display: block;
    width: 40px;
    height: 40px;
    margin: 0 auto 12px;
    border-radius: 50%;
    background: var(--brand-green);
  }
  .brand__name {
    display: block;
    font-size: 46px;
    line-height: 1;
  }
  .brand__tagline {
    display: block;
    margin-top: 10px;
    font-size: 18px;
    line-height: 1;
  }
  .headline {
    position: absolute;
    inset: 0;
    width: 1200px;
    height: 444px;
  }
  .headline text {
    fill: var(--ink);
    font-family: "Archivo Black", "Arial Black", sans-serif;
    text-transform: uppercase;
  }
</style>
</head>
<body>
  <main class="cover">
    <div class="cover__texture" role="img" aria-label="Light grey concrete texture background"></div>

    <div class="brand">
      <span class="brand__dot"></span>
      <span class="brand__name">K DORSEY</span>
      <span class="brand__tagline">SEPTIC SOLUTIONS LLC.</span>
    </div>

    <svg class="headline" viewBox="0 0 1200 444" role="heading" aria-level="1" aria-label="When last was the time you had your septic system serviced? If you can not remember it's been too long. Call today">
      <text x="374" y="50"  font-size="36" textLength="118" lengthAdjust="spacingAndGlyphs">WHEN</text>
      <text x="496" y="53"  font-size="67" textLength="169" lengthAdjust="spacingAndGlyphs">LAST</text>
      <text x="374" y="79"  font-size="36" textLength="94"  lengthAdjust="spacingAndGlyphs">WAS</text>
      <text x="374" y="113" font-size="40" textLength="94"  lengthAdjust="spacingAndGlyphs">THE</text>
      <text x="475" y="134" font-size="79" textLength="646" lengthAdjust="spacingAndGlyphs">TIME YOU HAD</text>
      <text x="374" y="194" font-size="50" textLength="795" lengthAdjust="spacingAndGlyphs">YOUR SEPTIC SYSTEM SERVICED ?</text>
      <text x="377" y="283" font-size="93" textLength="94"  lengthAdjust="spacingAndGlyphs">IF</text>
      <text x="477" y="245" font-size="32" textLength="60"  lengthAdjust="spacingAndGlyphs">YOU</text>
      <text x="477" y="274" font-size="36" textLength="154" lengthAdjust="spacingAndGlyphs">CAN NOT</text>
      <text x="638" y="269" font-size="64" textLength="166" lengthAdjust="spacingAndGlyphs">IT’S</text>
      <text x="808" y="262" font-size="38" textLength="111" lengthAdjust="spacingAndGlyphs">TOO</text>
      <text x="377" y="314" font-size="46" textLength="252" lengthAdjust="spacingAndGlyphs">REMEMBER</text>
      <text x="643" y="314" font-size="46" textLength="125" lengthAdjust="spacingAndGlyphs">BEEN</text>
      <text x="778" y="314" font-size="56" textLength="146" lengthAdjust="spacingAndGlyphs">LONG</text>
      <text x="377" y="391" font-size="60" textLength="415" lengthAdjust="spacingAndGlyphs">CALL TODAY</text>
    </svg>
  </main>
</body>
</html>
```